Successful Commercial Refrigeration business needs a flyer

We need a flyer (DL size) designed for our existing commercial refrigeration business. We are a family owned business, run by a father and son. We have been in operation since 1980 with the majority of our clients being based in Melbourne's South Eastern suburbs and we are now looking to get new clients in Melbourne's west.

Website can be accessed here http://coldhavenfridge.com.au/ to get further information on services we provide. Our main competitor is http://www.vortexchillworks.com.au/

Contact details are to be Trevor Hale, 0438 261 947, coldhaventh@mailbox.example
Updates

Hi All The majority of designs coming through are using images that have been pulled from the website. I'm happy for images to be use on the design (and just as happy for images not to be used) but I would prefer the images to be of front end equipment rather than backend (for instance, instead of showing the system thats on the roof, perhaps use a nice image of a bar or a cake fridge or something along those lines). We don't own these photos (they're from a competitor) but just wanted to give examples http://www.vortexchillworks.com.au/files/4013/7051/8196/IMG_2273.jpg http://www.vortexchillworks.com.au/files/3513/7051/8018/IMG_2267.JPG

Industry/Entity Type

Business

Requirements
Must have
• Contact details
Trevor Hale, 0438 261 947, coldhaventh@mailbox.example, www.coldhavenfridge.com.au

- services (info on websites listed in brief)

- refer to commercial refrigeration (not just refrigeration as we don't want domestic enquiries)

If there is going to be a call out regarding the area we service - please word it around "servicing all of melbourne"
my original brief explained that we were trying to build business in the western suburbs but now I realise that if we use that specific call out it will limit where we can send these flyers. So let's keep it generic.

```html
<!DOCTYPE html>
<html lang="en">
<head>
<meta charset="utf-8">
<title>Coldhaven Refrigeration – Flyer</title>
<link rel="stylesheet" href="https://fonts.googleapis.com/css2?family=Barlow+Semi+Condensed:wght@500;600;700&family=Open+Sans:wght@700&display=swap">
<style>
  :root {
    --blue: #7394c2;
    --navy: #26303f;
    --ink: #1f2630;
    --bg-start: #dde5f0;
    --bg-end: #ffffff;
    --icon: #5f8fb0;
    --page: #ffffff;
  }
  * { box-sizing: border-box; margin: 0; padding: 0; }
  html, body { width: 1200px; height: 650px; overflow: hidden; background: var(--page); }
  body { position: relative; font-family: "Barlow Semi Condensed", sans-serif; color: var(--ink); }

  .card-shadow-strip { position: absolute; left: 1129px; top: 50px; width: 23px; height: 550px; background: var(--navy); }
  .card {
    position: absolute; left: 50px; top: 50px; width: 1079px; height: 550px;
    background: linear-gradient(120deg, var(--bg-start) 0%, var(--bg-end) 80%);
    border: 1px solid #8a8f96; border-right: none;
  }
  .band-blue { position: absolute; left: 50px; top: 580px; width: 491px; height: 20px; background: var(--blue); }
  .band-navy { position: absolute; left: 601px; top: 580px; width: 551px; height: 20px; background: var(--navy); }

  .brand {
    position: absolute; left: 0; top: 108px; width: 1200px;
    display: flex; justify-content: center; align-items: flex-end; gap: 14px;
  }
  .brand-tag { font-family: "Open Sans", sans-serif; font-weight: 700; font-size: 10px; color: var(--ink); padding-bottom: 22px; }
  .brand-block { display: flex; flex-direction: column; align-items: flex-end; }
  .brand-name { font-weight: 700; font-size: 56px; line-height: 1; color: var(--blue); }
  .brand-est { font-family: "Open Sans", sans-serif; font-weight: 700; font-size: 11px; color: var(--ink); margin-top: 4px; }

  .tagline {
    position: absolute; left: 0; top: 210px; width: 1200px; text-align: center;
    font-weight: 500; font-size: 34px; line-height: 49px; color: var(--blue); letter-spacing: 0.5px;
  }
  .tagline .dark { color: var(--navy); }

  .services-box {
    position: absolute; left: 96px; top: 355px; width: 394px; height: 161px;
    background: #fff; box-shadow: 0 2px 10px rgba(40,60,90,0.25);
    padding: 10px 8px; font-weight: 500; font-size: 33px; line-height: 49px; color: var(--navy); letter-spacing: 0.4px;
  }

  .contact { position: absolute; left: 607px; top: 336px; }
  .contact-name { font-weight: 500; font-size: 40px; margin-left: 60px; color: var(--ink); letter-spacing: 0.5px; }
  .contact-list { list-style: none; margin-top: 8px; }
  .contact-item { display: flex; align-items: center; height: 50px; }
  .contact-item svg { width: 46px; height: 46px; flex: none; margin-right: 14px; }
  .contact-phone { font-weight: 500; font-size: 30px; letter-spacing: 0.5px; }
  .contact-text { font-weight: 500; font-size: 37px; }
</style>
</head>
<body>
  <div class="card-shadow-strip"></div>
  <div class="card"></div>
  <div class="band-blue"></div>
  <div class="band-navy"></div>

  <header class="brand">
    <span class="brand-tag">FULLY LICENSED</span>
    <div class="brand-block">
      <span class="brand-name">Coldhaven Refrigeration</span>
      <span class="brand-est">Est.1980</span>
    </div>
    <span class="brand-tag">PTY LTD</span>
  </header>

  <p class="tagline">All commercial refrigeration and air conditioning<br>servicing <span class="dark">all of Melbourne</span></p>

  <div class="services-box">For all your fridge, freezer,<br>cool room, bottle cabinets<br>and air conditioner needs</div>

  <section class="contact">
    <h2 class="contact-name">Trevor Hale</h2>
    <ul class="contact-list">
      <li class="contact-item">
        <svg viewBox="0 0 46 46" aria-hidden="true">
          <circle cx="23" cy="23" r="22" fill="#e8eef3" stroke="#b7c3cc"/>
          <circle cx="23" cy="23" r="18" fill="var(--icon)"/>
          <path d="M16 13c2-1 3 0 4 3s0 3-1 4c1 3 3 5 6 6 1-1 2-2 4-1s3 2 2 4c-1 2-3 3-6 2-6-2-10-7-11-12 0-3 1-5 2-6z" fill="#fff"/>
        </svg>
        <span class="contact-phone">0438 261 947</span>
      </li>
      <li class="contact-item">
        <svg viewBox="0 0 46 46" aria-hidden="true">
          <circle cx="23" cy="23" r="22" fill="#e8eef3" stroke="#b7c3cc"/>
          <circle cx="23" cy="23" r="18" fill="var(--icon)"/>
          <rect x="13" y="16" width="20" height="14" fill="#fff"/>
          <path d="M13 16l10 8 10-8" fill="none" stroke="var(--icon)" stroke-width="1.5"/>
        </svg>
        <span class="contact-text">coldhaventh@mailbox.example</span>
      </li>
      <li class="contact-item">
        <svg viewBox="0 0 46 46" aria-hidden="true">
          <circle cx="23" cy="23" r="22" fill="#e8eef3" stroke="#b7c3cc"/>
          <circle cx="23" cy="23" r="18" fill="var(--icon)"/>
          <path d="M12 23l11-10 11 10h-3v9H15v-9z" fill="#fff"/>
          <rect x="20" y="24" width="6" height="5" fill="var(--icon)"/>
        </svg>
        <span class="contact-text">www.coldhavenfridge.com.au</span>
      </li>
    </ul>
  </section>
</body>
</html>
```